Business card for different employees

A professional new updated design incorporating our current business's color themes and styles such as our on-site service trucks decals included in pictures attached. Our current business card is very simple and not professionally designed. We are a small family business but want a professional corporate look.

Target Market(s)

Cards to be handed out to new customers , corperate meetings. For our on site service operators.

Industry/Entity Type

Hydraulic

Contact Information for Business Card

Address, website, phone number, email, logo.
slogan - "Industry chosen hose and fittings provider".
24/7 on-site service , supply and hose management
Experienced , indpendant , family owned

Font styles to use
Sans Serif

Requirements
Must have
• Easily editable so that I can add different names and different roles for employees etc.
Nice to have
• Freedom with colour doesn't necessarily have to be blue but that is our company colour theme with trucks and logo so makes sense for the card to have blue like the trucks.

```html
<!DOCTYPE html>
<html lang="en">
<head>
<meta charset="utf-8">
<title>Meridian Hose and Fittings – Business Card</title>
<link rel="stylesheet" href="https://fonts.googleapis.com/css2?family=Jost:ital,wght@0,400;0,500;0,700;1,400&display=swap">
<style>
  :root {
    --brand-blue: #2f47a0;
    --ink-dark: #1c1c24;
    --paper: #ffffff;
    --stage: #3a3330;
    --text-grey: #2a2a30;
  }
  * { box-sizing: border-box; margin: 0; padding: 0; }
  html, body {
    width: 1200px; height: 716px; overflow: hidden;
    background: var(--stage);
    font-family: "Jost", "Helvetica Neue", Arial, sans-serif;
  }
  .canvas {
    position: relative; width: 1200px; height: 716px;
  }
  .card {
    position: absolute; width: 540px; height: 310px;
    overflow: hidden;
    box-shadow: 0 14px 30px rgba(0,0,0,0.45);
  }

  /* ---------- Front ---------- */
  .card-front {
    left: 40px; top: 120px;
    background: var(--brand-blue);
    color: var(--paper);
  }
  .front-brand {
    position: absolute; left: 0; right: 0; top: 92px;
    display: flex; align-items: center; justify-content: center; gap: 14px;
  }
  .brand-dot {
    width: 44px; height: 44px; border-radius: 50%;
    background: var(--ink-dark);
  }
  .brand-name {
    font-weight: 700; font-size: 30px; letter-spacing: 1px;
    text-transform: uppercase; line-height: 1;
  }
  .brand-sub {
    display: block; font-size: 13px; letter-spacing: 3px; margin-top: 6px;
    font-weight: 700;
  }
  .front-slogan {
    position: absolute; left: 0; right: 0; top: 232px;
    display: flex; align-items: center; gap: 16px;
    font-style: italic; font-size: 13px; letter-spacing: 0.3px;
  }
  .front-slogan .rule { height: 1px; background: var(--paper); }
  .front-slogan .rule-left { width: 80px; margin-left: 20px; }
  .front-slogan .rule-right { flex: 1; margin-right: 20px; }

  /* ---------- Back ---------- */
  .card-back {
    left: 620px; top: 286px;
    background: var(--paper);
    color: var(--text-grey);
  }
  .holder {
    position: absolute; left: 0; top: 34px;
    display: flex; gap: 12px;
  }
  .holder-accent { width: 12px; height: 44px; background: var(--brand-blue); }
  .holder-name {
    color: var(--brand-blue); font-weight: 700; font-size: 19px;
    letter-spacing: 0.5px; text-transform: uppercase; line-height: 1.1;
  }
  .holder-role { font-size: 11px; margin-top: 2px; }

  .back-brand {
    position: absolute; right: 36px; top: 104px;
    display: flex; align-items: center; gap: 10px;
    color: var(--brand-blue);
  }
  .back-brand .brand-dot { width: 34px; height: 34px; }
  .back-brand .brand-name { font-size: 22px; }
  .back-brand .brand-sub { font-size: 9.5px; letter-spacing: 2.2px; margin-top: 4px; }

  .divider {
    position: absolute; left: 24px; right: 24px; top: 178px;
    height: 1px; background: var(--brand-blue);
  }
  .contact {
    position: absolute; left: 24px; top: 188px;
    list-style: none; font-size: 10.5px; line-height: 1.55;
  }
  .contact li { display: flex; align-items: center; gap: 6px; }
  .contact svg { width: 9px; height: 9px; fill: var(--brand-blue); }
  .contact .accent { color: var(--brand-blue); }

  .services {
    position: absolute; right: 24px; top: 190px;
    list-style: none; text-align: right; font-size: 11px; line-height: 1.6;
  }
  .services .bullet { color: var(--brand-blue); margin-left: 4px; }

  .address-band {
    position: absolute; left: 0; right: 0; bottom: 0; height: 30px;
    background: var(--brand-blue); color: var(--paper);
    display: flex; align-items: center; padding-left: 24px;
    font-size: 11.5px; letter-spacing: 0.3px;
  }
</style>
</head>
<body>
<main class="canvas">

  <section class="card card-front" aria-label="Business card front">
    <div class="front-brand">
      <span class="brand-dot"></span>
      <div class="brand-name">Meridian<span class="brand-sub">Hose and Fittings</span></div>
    </div>
    <div class="front-slogan">
      <span class="rule rule-left"></span>
      <span class="slogan-text">Industry Chosen Hose And Fittings Provider</span>
      <span class="rule rule-right"></span>
    </div>
  </section>

  <section class="card card-back" aria-label="Business card back">
    <div class="holder">
      <span class="holder-accent"></span>
      <div>
        <p class="holder-name">Dana Whitfield</p>
        <p class="holder-role">Owner/CEO</p>
      </div>
    </div>

    <div class="back-brand">
      <span class="brand-dot"></span>
      <div class="brand-name">Meridian<span class="brand-sub">Hose and Fittings</span></div>
    </div>

    <div class="divider"></div>

    <ul class="contact">
      <li>
        <svg viewBox="0 0 10 10" aria-hidden="true"><path d="M2 0.5 L3.6 0.5 L4.2 3 L3 3.8 Q4 6 6.2 7 L7 5.8 L9.5 6.4 L9.5 8 Q9.5 9.5 8 9.5 Q0.5 9 0.5 2 Q0.5 0.5 2 0.5Z"/></svg>
        555-204-7781
      </li>
      <li>
        <svg viewBox="0 0 10 10" aria-hidden="true"><path d="M0 2 L10 2 L10 8 L0 8Z M0.6 2.4 L5 5.6 L9.4 2.4" stroke="#fff" stroke-width="0.7"/></svg>
        info@meridianhosefit.com
      </li>
      <li>
        <svg viewBox="0 0 10 10" aria-hidden="true"><circle cx="5" cy="5" r="4.6"/></svg>
        <span>www.<span class="accent">meridianhosefit</span>.com</span>
      </li>
    </ul>

    <ul class="services">
      <li>24/7 on-site service<span class="bullet">•</span></li>
      <li>Supply and Hose Management<span class="bullet">•</span></li>
      <li>Family Owned <span class="bullet">•</span> Independent <span class="bullet">•</span> Experienced<span class="bullet">•</span></li>
    </ul>

    <div class="address-band">1840 B Harlow Avenue Denton County 4417</div>
  </section>

</main>
</body>
</html>
```